Pizza box design for 12,14,16,18 and 20 inch pizza boxes

Hello, i need a pizza box design for various size pizza boxes (12,14,16,18 and 20 inches), please review website to get an idea for design

Design should include pizzeria logo, website and store locations and phone numbers
attached is the pizzeria logo

website: www.Ravellopiezaxy.com
Stores:
Lakeview 972-418-6307
Ashford 214-761-2938
Pine Ridge 682-140-3861

Industry/Entity Type

Pizzeria Restaurant

Colors

Designer to choose colors to be used in the design.

```html
<!DOCTYPE html>
<html lang="en">
<head>
<meta charset="utf-8">
<title>Ravello's Pizza – Box Dieline</title>
<link rel="stylesheet" href="https://fonts.googleapis.com/css2?family=Alfa+Slab+One&family=Roboto+Condensed:wght@700&family=Roboto+Slab:wght@700&display=swap">
<style>
  :root {
    --ink: #0d0b0a;
    --paper: #ffffff;
    --accent: #f6a545;
    --art-tone: #9a9590;
  }
  html, body {
    margin: 0;
    padding: 0;
    width: 821px;
    height: 1200px;
    overflow: hidden;
    background: var(--paper);
  }
  .canvas {
    position: relative;
    width: 821px;
    height: 1200px;
  }
  .dieline {
    position: absolute;
    left: 34px;
    top: 230px;
    width: 753px;
    height: 740px;
  }
  .panel { fill: var(--ink); }
  .lid-face { fill: var(--paper); }
  .tagline {
    font-family: "Roboto Condensed", sans-serif;
    font-weight: 700;
    font-size: 25px;
    fill: var(--accent);
    letter-spacing: 0.5px;
  }
  .brand-name {
    font-family: "Alfa Slab One", serif;
    font-size: 27px;
    fill: var(--ink);
  }
  .web-address {
    font-family: "Roboto Slab", serif;
    font-weight: 700;
    font-size: 13px;
    fill: var(--paper);
    letter-spacing: 0.8px;
  }
  .store-city, .store-phone {
    font-family: "Roboto Condensed", sans-serif;
    font-size: 11px;
    font-weight: 700;
  }
  .store-city { fill: var(--accent); }
  .store-phone { fill: var(--paper); }
  .rule { stroke: var(--paper); stroke-width: 0.6; }
  .illustration { fill: var(--art-tone); }
</style>
</head>
<body>
<main class="canvas">
  <svg class="dieline" viewBox="0 0 502 493" xmlns="http://www.w3.org/2000/svg">
    <defs>
      <path id="tagline-arc" d="M 84 290 A 166 166 0 0 1 416 290"/>
    </defs>

    <g class="flap flap-back">
      <rect class="panel" x="65" y="0" width="374" height="58"/>
      <g transform="rotate(180 252 29)">
        <text x="88" y="24"><tspan class="store-city">LAKEVIEW</tspan><tspan class="store-phone" dx="6">972-418-6307</tspan></text>
        <circle cx="253" cy="20" r="4" fill="var(--paper)"/>
        <text x="275" y="24"><tspan class="store-city">ASHFORD</tspan><tspan class="store-phone" dx="6">214-761-2938</tspan></text>
        <line class="rule" x1="80" y1="33" x2="424" y2="33"/>
        <text x="252" y="47" text-anchor="middle"><tspan class="store-city">PINE RIDGE</tspan><tspan class="store-phone" dx="6">682-140-3861</tspan></text>
      </g>
    </g>

    <g class="flap flap-left">
      <rect class="panel" x="0" y="63" width="58" height="365"/>
      <text class="web-address" transform="translate(25 245) rotate(90)" text-anchor="middle">www.Ravellopiezaxy.com</text>
    </g>
    <g class="flap flap-right">
      <rect class="panel" x="446" y="63" width="56" height="365"/>
      <text class="web-address" transform="translate(478 245) rotate(-90)" text-anchor="middle">www.Ravellopiezaxy.com</text>
    </g>

    <g class="lid">
      <rect class="lid-face" x="65" y="63" width="374" height="365"/>
      <path class="panel" d="M 65 63 H 439 V 303 H 377 V 278 A 115 115 0 0 0 147 278 V 303 H 65 Z"/>
      <text class="tagline"><textPath href="#tagline-arc" startOffset="50%" text-anchor="middle">Fresh From Our Oven Daily</textPath></text>
      <ellipse class="illustration" role="img" aria-label="Illustration of a torch-bearing statue figure" cx="255" cy="250" rx="70" ry="75"/>
      <text class="brand-name" x="252" y="375" text-anchor="middle" textLength="322" lengthAdjust="spacingAndGlyphs">RAVELLO'S PIZZA</text>
    </g>

    <g class="flap flap-front">
      <rect class="panel" x="65" y="435" width="374" height="58"/>
      <text x="88" y="459"><tspan class="store-city">LAKEVIEW</tspan><tspan class="store-phone" dx="6">972-418-6307</tspan></text>
      <circle cx="253" cy="455" r="4" fill="var(--paper)"/>
      <text x="275" y="459"><tspan class="store-city">ASHFORD</tspan><tspan class="store-phone" dx="6">214-761-2938</tspan></text>
      <line class="rule" x1="80" y1="466" x2="424" y2="466"/>
      <text x="252" y="482" text-anchor="middle"><tspan class="store-city">PINE RIDGE</tspan><tspan class="store-phone" dx="6">682-140-3861</tspan></text>
    </g>
  </svg>
</main>
</body>
</html>
```